We sell companies excess stock for them

We need a business card for a company based in New Zealand called 'ShelfLark'.

Check out our website to get an idea www.shelflark.example

We help other businesses to;
- Sell Excess Stock
- Manage Product Returns
- Sell Company Assets

Our logo is attached for your reference
The font used is 'RifficFree-Bold'

Target Market(s)

Businesses

Industry/Entity Type

Business

Contact Information for Business Card

Name: Mara Quillby
Phone: 027 864 3190
email: maraquillby@shelflark.example
website: www.shelflark.example

Font styles to use
Other font styles liked:

Colors
9bcb3b

Requirements
Must have
Nice to have
Should not have

```html
<!DOCTYPE html>
<html lang="en">
<head>
<meta charset="utf-8">
<title>ShelfLark Business Card</title>
<link rel="stylesheet" href="https://fonts.googleapis.com/css2?family=Open+Sans:wght@400;600;700&display=swap">
<style>
  :root {
    --green: #8dc23c;
    --ink: #2b2b2b;
    --text: #3a3a3a;
    --paper: #ffffff;
    --backdrop: #ecebe8;
    --art-yellow: #f4a93a;
    --art-green: #9bcb3b;
  }
  html, body {
    margin: 0;
    padding: 0;
    width: 1200px;
    height: 1000px;
    overflow: hidden;
    background: var(--backdrop);
    font-family: "Open Sans", Arial, sans-serif;
  }
  .card {
    position: absolute;
    left: 100px;
    top: 202px;
    width: 999px;
    height: 596px;
    background: var(--paper);
    box-shadow: 0 2px 8px rgba(0,0,0,0.12);
  }
  .brand-name {
    position: absolute;
    left: 56px;
    top: 108px;
    margin: 0;
    font-family: "Open Sans", Arial, sans-serif;
    font-weight: 700;
    font-size: 66px;
    letter-spacing: -2px;
    color: var(--ink);
    line-height: 1;
  }
  .person {
    position: absolute;
    left: 69px;
    top: 250px;
  }
  .person-name {
    margin: 0;
    font-weight: 600;
    font-size: 30px;
    color: var(--green);
    line-height: 36px;
  }
  .person-role {
    margin: 0;
    font-size: 24px;
    color: var(--text);
    line-height: 32px;
  }
  .address {
    position: absolute;
    left: 69px;
    top: 328px;
    margin: 0;
    font-style: normal;
    font-size: 24px;
    line-height: 33px;
    color: var(--text);
  }
  .contacts {
    position: absolute;
    left: 69px;
    top: 411px;
    margin: 0;
    padding: 0;
    list-style: none;
    font-size: 24px;
    line-height: 33px;
    color: var(--text);
  }
  .contacts li {
    display: flex;
    align-items: center;
    gap: 12px;
    height: 33px;
  }
  .contacts svg {
    width: 22px;
    height: 22px;
    fill: var(--green);
    flex: none;
  }
  .accent { color: var(--green); }
  .mascot-art {
    position: absolute;
    left: 479px;
    top: 47px;
    width: 472px;
    height: 502px;
    border-radius: 46% 40% 44% 38%;
    background: radial-gradient(ellipse at 55% 45%, var(--art-yellow) 0%, var(--art-green) 55%, rgba(155,203,59,0.25) 80%, rgba(255,255,255,0) 100%);
  }
</style>
</head>
<body>
  <section class="card">
    <h1 class="brand-name">ShelfLark</h1>

    <div class="person">
      <p class="person-name">MARA QUILLBY</p>
      <p class="person-role">Managing Director</p>
    </div>

    <address class="address">Harlow Bend, Marton,<br>Rangitikei, 4710</address>

    <ul class="contacts">
      <li>
        <svg viewBox="0 0 24 24" aria-hidden="true"><path d="M3 9c0-3 4-5 9-5s9 2 9 5v2h-5V9c-1-1-7-1-8 0v2H3zM6 12h12l2 8H4z"/></svg>
        027 864 3190
      </li>
      <li>
        <svg viewBox="0 0 24 24" aria-hidden="true"><path d="M7 3h10v5H7zM3 9h18v8h-3v-3H6v3H3zM7 15h10v6H7z"/></svg>
        + 000 000 0000
      </li>
      <li>
        <svg viewBox="0 0 24 24" aria-hidden="true"><path d="M2 5h20v14H2zM3.5 6.5 12 13l8.5-6.5z" fill-rule="evenodd"/></svg>
        maraquillby@shelflark.example
      </li>
      <li>
        <svg viewBox="0 0 24 24" aria-hidden="true"><circle cx="11" cy="11" r="8" fill="none" stroke="#8dc23c" stroke-width="2.5"/><path d="M11 10l10 4-4 1.5 3.5 3.5-2 2-3.5-3.5L13.5 21z"/></svg>
        <span>www.shelf<span class="accent">lark</span>.example</span>
      </li>
    </ul>

    <div class="mascot-art" role="img" aria-label="Cartoon delivery courier mascot in a green cap and overalls, giving a thumbs up while running with an orange parcel"></div>
  </section>
</body>
</html>
```